Italian restaurant needs new site

Need to make our website better.

Must have reservation module

Must be able to sell wine tasting tours and wine pairing tours and intégrate with lumo desk

Blog

Social media

Wandermeter ranking and last review.

Number of Pages Required

1 page

Font styles to use
Serif

Requirements
Must have
• Reservation module
• Marketplace to buy wine pairings and gift certificates
• Wandermeter review
• Chatterbay posts
• All info from old site

```html
<!DOCTYPE html>
<html lang="en">
<head>
<meta charset="utf-8">
<title>Vinora Bistro – Italian Restaurant in Puerto Alba</title>
<link href="https://fonts.googleapis.com/css2?family=Raleway:wght@400;500;600;700;800&display=swap" rel="stylesheet">
<style>
:root{
  --wine:#8a1c22;
  --wine-deep:#5a0f14;
  --orange:#f7901e;
  --ink:#2d2d2d;
  --body:#6b6b6b;
  --light:#f3f3f3;
  --footer:#2b2b2b;
  --footer-base:#1e1e1e;
  --white:#ffffff;
  --rating:#00a680;
}
*{box-sizing:border-box;margin:0;padding:0}
html,body{width:1200px;height:2723px;overflow:hidden}
body{font-family:"Raleway",sans-serif;color:var(--ink);background:var(--white);position:relative}
.abs{position:absolute}

/* header */
.site-header{position:absolute;left:0;top:0;width:1200px;height:127px;background:var(--white)}
.brand{position:absolute;left:74px;top:40px;display:flex;align-items:center;gap:10px}
.brand-mark{width:14px;height:14px;background:var(--wine)}
.brand-name{font-size:24px;font-weight:600;color:var(--wine)}
.main-nav{position:absolute;top:60px;left:400px;right:74px;display:flex;justify-content:space-between}
.main-nav a{font-size:13px;font-weight:600;color:var(--ink);text-decoration:none;letter-spacing:.3px;position:relative}
.main-nav a.active{color:var(--wine)}
.main-nav a.active::after{content:"";position:absolute;left:-7px;right:-7px;top:23px;height:4px;background:var(--wine)}

/* hero */
.hero{position:absolute;left:0;top:127px;width:1200px;height:536px;
  background:radial-gradient(ellipse at 55% 55%,#d98a3a 0%,#8a4a1e 35%,#3a1d10 75%,#1e0f08 100%)}
.hero-title{position:absolute;left:0;right:0;top:228px;text-align:center;color:var(--white);
  font-size:31px;font-weight:700;line-height:39px;letter-spacing:.5px}
.hero-title span{background:rgba(0,0,0,.45);padding:0 10px}
.hero-dots{position:absolute;top:489px;left:560px;display:flex;gap:9px}
.hero-dots i{width:13px;height:13px;border-radius:50%;background:var(--white)}
.hero-dots i:first-child{background:var(--orange)}

/* reservations */
.reservations{position:absolute;left:0;top:663px;width:1200px;height:319px;
  background:linear-gradient(100deg,#3a0b0e 0%,var(--wine-deep) 35%,#7c1a20 100%)}
.res-title{position:absolute;left:74px;top:46px;color:var(--white);font-size:25px;font-weight:700;display:flex;align-items:center;gap:14px}
.field{position:absolute;height:44px;background:var(--white);border-radius:2px;font-size:13px;color:#777;
  padding:0 16px;display:flex;align-items:center;justify-content:space-between}
.submit{position:absolute;height:44px;background:var(--orange);color:var(--white);font-weight:700;font-size:15px;
  display:flex;align-items:center;justify-content:center;letter-spacing:.5px}

/* feature sections */
.feature{position:absolute;left:0;width:1200px;height:400px;background:var(--white)}
.feature-photo{position:absolute;top:0;height:400px}
.feature h2{position:absolute;font-size:25px;font-weight:700;color:#333;letter-spacing:.3px}
.feature p{position:absolute;width:470px;font-size:14px;line-height:24.5px;color:var(--body)}
.btn-more{position:absolute;width:182px;height:49px;background:var(--wine);color:var(--white);
  font-size:13px;font-weight:700;display:flex;align-items:center;justify-content:center;letter-spacing:.3px}

/* blog */
.blog{position:absolute;left:0;top:1781px;width:1200px;height:481px;background:var(--light)}
.blog h2{position:absolute;left:0;right:0;top:52px;text-align:center;font-size:25px;font-weight:600;color:#333}
.post{position:absolute;top:118px;width:331px}
.post-photo{width:331px;height:185px}
.post h3{margin-top:26px;font-size:15px;font-weight:700;color:var(--wine);letter-spacing:.2px}
.post p{margin-top:9px;font-size:14px;line-height:21px;color:var(--body)}

/* footer */
.site-footer{position:absolute;left:0;top:2262px;width:1200px;height:383px;background:var(--footer);color:var(--white)}
.site-footer h4{position:absolute;top:49px;font-size:17px;font-weight:700}
.contact{position:absolute;left:74px;top:93px;font-size:14px;line-height:21px;color:#ddd}
.hours{position:absolute;left:74px;top:170px;font-size:14px;font-weight:700}
.map{position:absolute;left:74px;top:206px;width:331px;height:131px;background:linear-gradient(135deg,#dfe6ea,#c7d6e0 60%,#a9c3d6)}
.widget{position:absolute;top:92px;width:331px;height:245px;background:var(--white);color:var(--ink)}
.wm-head{position:absolute;left:14px;top:16px;display:flex;align-items:center;gap:7px;font-size:17px;font-weight:600;color:#222}
.wm-head i{width:12px;height:12px;border-radius:50%;background:var(--rating)}
.wm-tag{position:absolute;left:14px;top:46px;font-size:10px;color:#777}
.wm-line{position:absolute;left:0;right:0;height:1px;background:#ddd}
.wm-name{position:absolute;left:22px;top:90px;font-size:13px;font-weight:600;text-decoration:underline}
.wm-label{position:absolute;left:22px;font-size:10px;font-weight:700}
.wm-dots{position:absolute;left:22px;top:128px;display:flex;gap:2px}
.wm-dots i{width:11px;height:11px;border-radius:50%;background:var(--rating)}
.wm-small{position:absolute;left:22px;top:144px;font-size:8px;color:#999}
.wm-rank{position:absolute;left:22px;top:202px;font-size:11px;line-height:14px;color:var(--rating)}
.wm-rank b{color:#333;font-weight:600}
.cb-cover{position:absolute;left:0;top:0;width:331px;height:122px;background:linear-gradient(135deg,#a0141b,#d23a3a 50%,#7a0d12)}
.cb-thumb{position:absolute;left:14px;top:16px;width:56px;height:56px;background:#4a0c10;border:2px solid var(--white)}
.cb-name{position:absolute;left:84px;top:22px;font-size:18px;font-weight:700;color:var(--white)}
.cb-likes{position:absolute;left:84px;top:45px;font-size:11px;color:var(--white)}
.cb-btn{position:absolute;left:14px;top:88px;background:var(--white);font-size:10px;font-weight:700;color:#3b5998;padding:3px 6px}
.cb-text{position:absolute;left:14px;top:132px;font-size:11px;line-height:14px;color:#333;width:290px}
.cb-friends{position:absolute;left:14px;top:170px;display:flex;gap:4px}
.cb-friends i{width:52px;height:52px;background:linear-gradient(135deg,#8d7868,#4d5766)}

.base-bar{position:absolute;left:0;top:2645px;width:1200px;height:78px;background:var(--footer-base)}
.copyright{position:absolute;left:74px;top:32px;font-size:11px;color:#aaa}
.social{position:absolute;right:36px;top:28px;display:flex;gap:18px;align-items:center}
.social span{font-size:12px;font-weight:600;color:#bbb}
</style>
</head>
<body>

<header class="site-header">
  <div class="brand"><span class="brand-mark"></span><span class="brand-name">Vinora Bistro</span></div>
  <nav class="main-nav">
    <a class="active" href="#">HOME</a><a href="#">MENU</a><a href="#">RESERVATION</a><a href="#">WINE</a>
    <a href="#">WINE PAIRING TOURS</a><a href="#">BLOG</a><a href="#">CONTACT US</a>
  </nav>
</header>

<section class="hero" role="img" aria-label="Evening terrace of the restaurant with umbrellas and warm lighting">
  <h1 class="hero-title"><span>VINORA BISTRO ITALIAN RESTAURANT</span><br><span>IN PUERTO ALBA</span></h1>
  <div class="hero-dots"><i></i><i></i><i></i><i></i></div>
</section>

<section class="reservations">
  <h2 class="res-title">RESERVATIONS
    <svg width="26" height="16" viewBox="0 0 26 16"><path d="M0 8h22M15 1l8 7-8 7" stroke="#fff" stroke-width="3" fill="none"/></svg>
  </h2>
  <div class="field" style="left:74px;top:101px;width:244px">Name</div>
  <div class="field" style="left:343px;top:101px;width:241px">Email Address</div>
  <div class="field" style="left:613px;top:101px;width:242px">Phone No.</div>
  <div class="field" style="left:884px;top:101px;width:241px">Party Size
    <svg width="10" height="6"><path d="M1 1l4 4 4-4" stroke="#777" fill="none"/></svg></div>
  <div class="field" style="left:74px;top:159px;width:244px">Date
    <svg width="13" height="13"><rect x="1" y="2" width="11" height="10" fill="none" stroke="#777"/><rect x="1" y="2" width="11" height="3" fill="#777"/></svg></div>
  <div class="field" style="left:343px;top:159px;width:241px">Time
    <svg width="13" height="13"><circle cx="6.5" cy="6.5" r="5.5" fill="none" stroke="#777"/><path d="M6.5 3.5v3h2" stroke="#777" fill="none"/></svg></div>
  <div class="field" style="left:613px;top:159px;width:242px">Hotel Name</div>
  <div class="field" style="left:884px;top:159px;width:241px">Room Number</div>
  <div class="field" style="left:74px;top:217px;width:244px">Guest Email</div>
  <div class="field" style="left:343px;top:217px;width:512px">Comments (Optional)</div>
  <div class="submit" style="left:884px;top:217px;width:241px">SUBMIT</div>
</section>

<section class="feature" style="top:982px">
  <div class="feature-photo" role="img" aria-label="Guests tasting red wine in a barrel cellar"
       style="left:0;width:626px;clip-path:polygon(0 0,577px 0,626px 100%,0 100%);background:linear-gradient(120deg,#3b2418,#7a4a2e 50%,#c9b49a)"></div>
  <h2 style="left:662px;top:58px">SELL WINE TASTING TOURS</h2>
  <p style="left:662px;top:102px">Aliquam molestie, mi et imperdiet euismod, dui purus auctor tellus, et interdum lacus lectus et ante. Sed accumsan sollicitudin sapien, sit amet adipiscing turpis gravida ac. In congue, neque ac lobortis volutpat, libero mauris varius mi, vitae suscipit ipsum ligula vitae risus. Duis aliquam nibh a dui iaculis viverra id a velit.</p>
  <div class="btn-more" style="left:664px;top:278px">READ MORE</div>
</section>

<section class="feature" style="top:1382px">
  <div class="feature-photo" role="img" aria-label="Cheese board, small plates and glasses of red and white wine on a table"
       style="left:577px;width:623px;clip-path:polygon(49px 0,100% 0,100% 100%,0 100%);background:linear-gradient(135deg,#2e2a26,#6d5c48 45%,#b59c72 75%,#8a6a45)"></div>
  <h2 style="left:74px;top:58px">WINE PAIRING TOURS</h2>
  <p style="left:74px;top:102px">Aliquam molestie, mi et imperdiet euismod, dui purus auctor tellus, et interdum lacus lectus et ante. Sed accumsan sollicitudin sapien, sit amet adipiscing turpis gravida ac. In congue, neque ac lobortis volutpat, libero mauris varius mi, vitae suscipit ipsum ligula vitae risus. Duis aliquam nibh a dui iaculis viverra id a velit.</p>
  <div class="btn-more" style="left:74px;top:282px">READ MORE</div>
</section>

<section class="blog">
  <h2>BLOG</h2>
  <article class="post" style="left:74px">
    <div class="post-photo" role="img" aria-label="Plate of pasta with bread and wine" style="background:linear-gradient(135deg,#5a3a22,#c8833f 50%,#e8dccb)"></div>
    <h3>VESTIBULUM ANTE IPSUM PRIMIS</h3>
    <p>Aliquam molestie, mi et imperdiet euismod, dui purus auctor tellus, et interdum lacus lectus et ante..</p>
  </article>
  <article class="post" style="left:436px">
    <div class="post-photo" role="img" aria-label="Restaurant dining room at night" style="background:linear-gradient(135deg,#5a1216,#2a1a16 55%,#1a1210)"></div>
    <h3>VESTIBULUM ANTE IPSUM PRIMIS</h3>
    <p>Aliquam molestie, mi et imperdiet euismod, dui purus auctor tellus, et interdum lacus lectus et ante..</p>
  </article>
  <article class="post" style="left:793px">
    <div class="post-photo" role="img" aria-label="Restaurant terrace with umbrellas in the evening" style="background:linear-gradient(135deg,#3a1d10,#b0652a 55%,#e0a050)"></div>
    <h3>VESTIBULUM ANTE IPSUM PRIMIS</h3>
    <p>Aliquam molestie, mi et imperdiet euismod, dui purus auctor tellus, et interdum lacus lectus et ante..</p>
  </article>
</section>

<footer class="site-footer">
  <h4 style="left:74px">CONTACT INFO</h4>
  <h4 style="left:436px">WANDERMETER</h4>
  <h4 style="left:795px">FOLLOW US CHATTERBAY</h4>

  <div class="contact">Calle Olmo 14, Centro<br>Puerto Alba,<br>Costa Serena</div>
  <div class="hours">Open daily from 5 to 12 am</div>
  <div class="map" role="img" aria-label="Street map showing the restaurant location"></div>

  <div class="widget" style="left:436px">
    <div class="wm-head"><i></i>Wandermeter</div>
    <div class="wm-tag">Read more. Plan more. Eat well.</div>
    <div class="wm-line" style="top:66px"></div>
    <div class="wm-name">Vinora Bistro</div>
    <div class="wm-label" style="top:112px">Wandermeter Traveler Rating</div>
    <div class="wm-dots"><i></i><i></i><i></i><i></i><i></i></div>
    <div class="wm-small">Based on 1,200 traveler reviews</div>
    <div class="wm-line" style="left:22px;right:22px;top:168px"></div>
    <div class="wm-label" style="top:184px">Wandermeter Ranking</div>
    <div class="wm-rank"><b>#9</b> of 572 places to eat in Puerto<br>Alba</div>
  </div>

  <div class="widget" style="left:795px">
    <div class="cb-cover"></div>
    <div class="cb-thumb"></div>
    <div class="cb-name">Vinora Bistro</div>
    <div class="cb-likes">3,464 Me gusta</div>
    <div class="cb-btn">Me gusta esta página</div>
    <div class="cb-text">Sé el primero de tus amigos en indicar que te gusta esto.</div>
    <div class="cb-friends" role="img" aria-label="Profile pictures of followers"><i></i><i></i><i></i><i></i><i></i></div>
  </div>
</footer>

<div class="base-bar">
  <div class="copyright">Copyright © 2017. Company Name. All Right Reserved</div>
  <div class="social"><span>Chatterbay</span><span>Chirper</span><span>Pictagram</span><span>Workly</span><span>Streamly</span></div>
</div>

</body>
</html>
```